Finch Haulage Ltd

We need an A5 size (UK size) flyer to advertise our new business which is called Finch Haulage.
Domestic and Commercial Waste Clearance Services.
Please have the question in bold "Do you have a pile of junk you need to dispose of?"
We collect all kinds of junk or rubbish from homes and businesses across Kent, Sussex and South London.
No fuss, no mess!
A low cost, hassle free alternative to skip hire.
Licensed by the Landcare Board and fully insured (this can be in small print at the bottom).
Please put the Recycle symbol somewhere.
Our tagline on our vehicle is "We Clear More, For Less!"
We'd like the flyer to be bold and eye-catching (to catch the eye of the homeowner or business owner while it's sitting on their doormat).
We need our telephone, website and email to be prominent. Maybe saying "Call today for a free quote"
Tel. 01734 586019
Email: info@finchhaulage.example.co.uk
www.finchhaulage.example.co.uk
Target Market(s)
Our market will be homes and small businesses around Kent, Sussex and South London.

```html
<!DOCTYPE html>
<html lang="en">
<head>
<meta charset="utf-8">
<title>Finch Haulage – Waste Clearance Flyer</title>
<link href="https://fonts.googleapis.com/css2?family=Arimo:ital,wght@0,400;0,700;1,700&display=swap" rel="stylesheet">
<style>
  :root {
    --forest: #1e3a2e;
    --ink: #1f4a38;
    --brand-grey: #454545;
    --leaf: #1f9a4c;
    --paper: #ffffff;
    --backdrop: #d9d9d6;
    --photo-mall-a: #b9b6ae;
    --photo-mall-b: #6d6a62;
    --photo-junk-a: #b5664a;
    --photo-junk-b: #26304f;
  }
  * { margin: 0; padding: 0; box-sizing: border-box; }
  html, body { width: 1200px; height: 1000px; overflow: hidden; }
  body {
    background: var(--backdrop);
    font-family: "Arimo", Arial, sans-serif;
    position: relative;
  }
  .flyer {
    position: absolute; left: 302px; top: 77px;
    width: 598px; height: 846px;
    background: var(--paper);
  }
  .brand-name {
    position: absolute; left: 34px; top: 78px;
    font-size: 31px; font-weight: 700; color: var(--brand-grey);
    letter-spacing: 0.5px;
    display: flex; align-items: center; gap: 10px;
  }
  .brand-dot { width: 16px; height: 16px; border-radius: 50%; background: var(--leaf); }
  .contact-list {
    position: absolute; left: 296px; top: 64px;
    list-style: none; color: var(--ink); font-size: 21px; line-height: 27px;
  }
  .contact-list li { display: flex; align-items: center; gap: 9px; white-space: nowrap; }
  .contact-list li.contact-small { font-size: 17.5px; }
  .contact-list svg { width: 22px; height: 18px; flex: none; }
  .rule-double {
    position: absolute; left: 0; top: 190px; width: 100%; height: 15px;
    border-top: 5px solid var(--forest); border-bottom: 5px solid var(--forest);
  }
  .photo { position: absolute; top: 213px; height: 213px; }
  .photo-venue { left: 0; width: 308px; background: linear-gradient(180deg, var(--photo-mall-a), var(--photo-mall-b)); }
  .photo-junk { left: 312px; width: 286px; background: linear-gradient(160deg, var(--photo-junk-a) 0%, var(--photo-junk-b) 55%, #9a948a 100%); }
  .rule-squares {
    position: absolute; left: 0; top: 440px; width: 100%; height: 7px;
    background: repeating-linear-gradient(90deg, var(--forest) 0 7px, transparent 7px 13px);
  }
  .headline-box {
    position: absolute; left: 18px; top: 469px; width: 563px; height: 95px;
    background: var(--forest); color: var(--paper);
    font-weight: 700; font-size: 38px; line-height: 38px; text-align: center;
    display: flex; align-items: center; justify-content: center;
  }
  .rule-dots {
    position: absolute; left: 0; top: 583px; width: 100%; height: 3px;
    background: repeating-linear-gradient(90deg, var(--forest) 0 3px, transparent 3px 6px);
  }
  .service-copy {
    position: absolute; left: 30px; top: 602px;
    font-size: 23px; line-height: 27px; color: var(--forest);
    white-space: nowrap;
  }
  .rule-dashed-double {
    position: absolute; left: 29px; top: 695px; width: 542px; height: 8px;
    background:
      repeating-linear-gradient(90deg, var(--forest) 0 4px, transparent 4px 6px) top / 100% 4px no-repeat,
      linear-gradient(var(--forest), var(--forest)) bottom / 100% 3px no-repeat;
  }
  .tagline {
    position: absolute; left: 0; width: 100%; top: 718px;
    text-align: center; font-style: italic; font-weight: 700;
    font-size: 43px; line-height: 43px; color: var(--forest);
  }
  .recycle-mark { position: absolute; left: 499px; top: 753px; width: 66px; height: 62px; }
  .licence-bar {
    position: absolute; left: 0; bottom: 0; width: 100%; height: 24px;
    background: var(--leaf); color: var(--paper);
    font-size: 14.5px; line-height: 24px; padding-left: 11px;
  }
</style>
</head>
<body>
  <main class="flyer">
    <div class="brand-name"><span class="brand-dot"></span>Finch Haulage</div>

    <ul class="contact-list">
      <li>
        <svg viewBox="0 0 22 18"><path fill="#1f4a38" d="M2 5c0-2 3-3 9-3s9 1 9 3v2h-5V5H7v2H2z M5 8h12l2 8H3z"/><circle cx="11" cy="12" r="2.2" fill="#fff"/></svg>
        01734 586019
      </li>
      <li class="contact-small">
        <svg viewBox="0 0 22 18"><rect x="3" y="4" width="16" height="11" fill="#1f4a38"/><path d="M3 4l8 6 8-6" fill="none" stroke="#fff" stroke-width="1.5"/></svg>
        info@finchhaulage.example.co.uk
      </li>
      <li class="contact-small">
        <svg viewBox="0 0 22 18"><circle cx="11" cy="9" r="8" fill="#1f4a38"/><path d="M7 4c3 1 2 4 5 4s1 5 3 6M4 10c2 0 3 1 3 4" fill="none" stroke="#fff" stroke-width="1.6"/></svg>
        www.finchhaulage.example.co.uk
      </li>
    </ul>

    <div class="rule-double"></div>

    <div class="photo photo-venue" role="img" aria-label="Photo of a busy shopping centre atrium with people walking"></div>
    <div class="photo photo-junk" role="img" aria-label="Photo of a discarded blue sofa piled with an old television and bags against a brick wall"></div>

    <div class="rule-squares"></div>

    <h1 class="headline-box">Do you have a pile of junk<br>you need to dispose of?</h1>

    <div class="rule-dots"></div>

    <p class="service-copy">
      We collect all kinds of junk or rubbish<br>
      from homes and business.<br>
      No fuss, no mess! Very competitive prices.
    </p>

    <div class="rule-dashed-double"></div>

    <p class="tagline">“We Clear More,<br>For Less!"</p>

    <svg class="recycle-mark" viewBox="-31 -30 62 60" role="img" aria-label="Recycle symbol">
      <g id="chase-arrow" fill="#1f9a4c" stroke="#1f9a4c">
        <line x1="-20.5" y1="9.5" x2="-9.5" y2="-9.6" stroke-width="7"/>
        <polygon points="-2.2,-22.5 -1.8,-5.2 -17,-14" stroke="none"/>
      </g>
      <use href="#chase-arrow" transform="rotate(120)"/>
      <use href="#chase-arrow" transform="rotate(240)"/>
    </svg>

    <footer class="licence-bar">Licensed by the Landcare Board and fully insured</footer>
  </main>
</body>
</html>
```